A new presentation to our clients

we are a Real Estate agency, our website is www.dorelumia.com and it’s time to have a new, fashion and remarcable Business Card. we want to differentiate ourselves from other companies so we want a business card that differentiates us. we want the business card to impact our customers. in the competitive market that we have today, we have to be different and it is this difference that we seek

Target Market(s)

Real Estate Clients

Contact Information for Business Card

We search a totaly diferent card from the usual

Font styles to use
Sans Serif

Colors
e34197

Requirements
Must have
• Logo, adress, phone contact, e-mail, photo, and our website
Nice to have
• We would like to see a modern business card
Should not have
• Houses or building draws

```html
<!DOCTYPE html>
<html lang="en">
<head>
<meta charset="utf-8">
<title>Dore Lumia – Business Card</title>
<link rel="stylesheet" href="https://fonts.googleapis.com/css2?family=Didact+Gothic&family=Poppins:wght@600&display=swap">
<style>
  :root {
    --brand-pink: #ec2f78;
    --card-white: #ffffff;
    --backdrop: #e9ecf1;
    --photo-tone-a: #c9b6a6;
    --photo-tone-b: #2a3247;
  }
  * { margin: 0; padding: 0; box-sizing: border-box; }
  html, body { width: 1200px; height: 900px; overflow: hidden; }
  body {
    background: var(--backdrop);
    font-family: "Didact Gothic", "Century Gothic", sans-serif;
    position: relative;
  }
  .business-card {
    position: absolute;
    left: 226px; top: 236px;
    width: 748px; height: 428px;
    border-radius: 16px;
    overflow: hidden;
    background: var(--card-white);
    box-shadow: 0 10px 30px rgba(30, 40, 60, 0.18);
  }
  .brand-name {
    position: absolute;
    left: 55px; top: 30px;
    font-size: 56px;
    line-height: 1;
    color: var(--brand-pink);
    letter-spacing: 1px;
  }
  .rule-top {
    position: absolute;
    left: 0; top: 138px;
    width: 100%; height: 3px;
    background: var(--brand-pink);
  }
  .pink-band {
    position: absolute;
    left: 0; top: 146px;
    width: 100%; height: 282px;
    background: var(--brand-pink);
  }
  .rule-bottom {
    position: absolute;
    left: 0; top: 414px;
    width: 100%; height: 3px;
    background: var(--card-white);
  }
  .portrait-frame {
    position: absolute;
    left: 473px; top: 24px;
    width: 216px; height: 216px;
    border-radius: 50%;
    background: var(--card-white);
    border: 4px solid var(--brand-pink);
    padding: 4px;
  }
  .portrait {
    width: 100%; height: 100%;
    border-radius: 50%;
    background: radial-gradient(circle at 50% 35%, var(--photo-tone-a) 0 30%, #f3f1ee 31% 55%, var(--photo-tone-b) 56%);
  }
  .person {
    position: absolute;
    left: 431px; top: 243px;
    width: 300px;
    text-align: center;
    color: var(--card-white);
  }
  .person-name {
    font-family: "Poppins", sans-serif;
    font-weight: 600;
    font-size: 21px;
    line-height: 1.2;
  }
  .person-role {
    font-size: 17px;
    margin-top: 4px;
  }
  .address {
    position: absolute;
    right: 53px; top: 327px;
    text-align: right;
    color: var(--card-white);
    font-size: 17px;
    line-height: 26px;
  }
  .contact-list {
    position: absolute;
    left: 58px; top: 276px;
    list-style: none;
    color: var(--card-white);
    font-size: 17px;
    line-height: 26px;
  }
  .contact-list li { display: flex; align-items: center; }
  .contact-icon {
    width: 16px; height: 16px;
    margin-right: 15px;
    fill: var(--card-white);
    flex: none;
  }
</style>
</head>
<body>
  <div class="business-card">
    <div class="brand-name">Dore Lumia</div>
    <div class="rule-top"></div>
    <div class="pink-band"></div>
    <div class="rule-bottom"></div>

    <div class="portrait-frame">
      <div class="portrait" role="img" aria-label="Portrait photo of the company founder"></div>
    </div>

    <div class="person">
      <div class="person-name">Martin Ashford</div>
      <div class="person-role">CEO/Founder</div>
    </div>

    <div class="address">
      <div>Rua das Flores, 418</div>
      <div>4050-262, Porto</div>
    </div>

    <ul class="contact-list">
      <li>
        <svg class="contact-icon" viewBox="0 0 16 16" aria-hidden="true"><path d="M3.5 1.5l2.5 0 1 3.5-1.8 1.3c.9 1.9 2.5 3.5 4.4 4.4l1.3-1.8 3.5 1v2.5c0 .8-.7 1.5-1.5 1.5C7.3 14 2 8.7 2 3c0-.8.7-1.5 1.5-1.5z"/></svg>
        <span>(+351) 224 518 260</span>
      </li>
      <li>
        <svg class="contact-icon" viewBox="0 0 16 16" aria-hidden="true"><rect x="4" y="1.5" width="8" height="4"/><rect x="1" y="6" width="14" height="6" rx="1"/><rect x="4" y="10" width="8" height="4.5" fill="#ec2f78"/><rect x="5" y="11" width="6" height="3"/></svg>
        <span>(+351) 224 518 269</span>
      </li>
      <li>
        <svg class="contact-icon" viewBox="0 0 16 16" aria-hidden="true"><path d="M1 3h14v10H1z M2.5 4.5v.4L8 9l5.5-4.1v-.4z" fill-rule="evenodd"/></svg>
        <span>geral@dorelumia.com</span>
      </li>
      <li>
        <svg class="contact-icon" viewBox="0 0 16 16" aria-hidden="true" fill="none" stroke="#fff" stroke-width="1.3"><circle cx="8" cy="8" r="6.5"/><ellipse cx="8" cy="8" rx="3" ry="6.5"/><path d="M1.5 8h13M2.5 4.8h11M2.5 11.2h11"/></svg>
        <span>www.dorelumia.com</span>
      </li>
    </ul>
  </div>
</body>
</html>
```